KPR Tidy Yard Website

We need a website design for this new company. I've attached the company logo. This company is in the construction industry that provides general labor, maintenance and cleaning for construction sites. We want a clean and simple website that can be easy to navigate.

Target Market(s)

Construction industry

Industry/Entity Type

Construction

Number of Pages Required

2 page

Font styles to use
Sans Serif

```html
<!DOCTYPE html>
<html lang="en">
<head>
<meta charset="utf-8">
<title>KPR Tidy Yard</title>
<link rel="stylesheet" href="https://fonts.googleapis.com/css2?family=Montserrat:wght@400;500;600;700;800&display=swap">
<style>
:root{
  --orange:#ff5a0a;
  --navy:#0a0a72;
  --ink:#222;
  --grey:#555;
  --mint:#f0f5ee;
  --line:#e3e3e3;
  --black:#050505;
  --white:#fff;
}
*{box-sizing:border-box;margin:0;padding:0}
html,body{width:712px;height:1200px;overflow:hidden;background:var(--white)}
body{position:relative;font-family:"Montserrat",sans-serif;color:var(--ink)}
.abs{position:absolute}

/* header */
.site-header{left:0;top:0;width:712px;height:39px;background:var(--white)}
.brand{left:84px;top:9px;display:flex;align-items:center;gap:5px;font-size:11px;font-weight:800;color:var(--navy)}
.brand-mark{width:10px;height:10px;background:var(--orange)}
.main-nav{right:17px;top:16px;display:flex;gap:21px;font-size:6.6px;font-weight:600;color:var(--ink);letter-spacing:.2px}

/* hero */
.hero{left:0;top:39px;width:712px;height:268px;background:linear-gradient(120deg,#6a6c70 0%,#505256 45%,#3d3f43 100%)}
.hero-photo{left:380px;top:39px;width:332px;height:240px;background:radial-gradient(ellipse at 60% 40%,#7a7c80 0%,#55575b 55%,rgba(80,82,86,0) 80%)}
.hero-curve{left:0;top:270px}
.hero-title{left:88px;top:114px;font-size:22px;font-weight:700;line-height:26px;color:var(--white);letter-spacing:.6px}
.hero-text{left:96px;top:173px;width:320px;font-size:8.6px;line-height:10px;color:var(--white)}
.btn-orange{background:var(--orange);color:var(--white);font-weight:700;display:flex;align-items:center;justify-content:center}
.hero-btn{left:93px;top:207px;width:86px;height:23px;font-size:7.2px;letter-spacing:.4px}
.slide-arrow{width:23px;height:21px;background:rgba(20,20,20,.75)}
.slide-prev{left:49px;top:162px}
.slide-next{left:645px;top:162px}

/* services */
.services-band{left:0;top:321px;width:712px;height:303px;background:var(--mint)}
.service-card{background:var(--white);padding:7px;box-shadow:0 1px 5px rgba(0,0,0,.2)}
.service-card .photo{width:100%;height:114px}
.service-card .body{background:var(--mint);text-align:center;padding:8px 9px 0;height:calc(100% - 114px)}
.service-card h3{font-size:8.6px;font-weight:700;letter-spacing:.5px;margin-bottom:7px}
.service-card p{font-size:6.2px;line-height:11px;color:var(--grey)}
.card-labour{left:79px;top:281px;width:174px;height:194px}
.card-maintenance{left:270px;top:262px;width:175px;height:196px}
.card-cleaning{left:460px;top:281px;width:175px;height:194px}
.photo-site{background:linear-gradient(135deg,#a89c86,#7a8c92)}
.photo-helmet{background:linear-gradient(135deg,#8a4a3a,#d8b22a 55%,#b08a5a)}
.photo-wash{background:linear-gradient(135deg,#8a8478,#b8b2a6 55%,#6a7a6a)}

.welcome-title{left:0;top:519px;width:712px;text-align:center;font-size:11px;font-weight:700;color:#4a4a4a;letter-spacing:.2px}
.welcome-text{left:125px;top:548px;width:466px;text-align:center;font-size:6.1px;line-height:14px;color:var(--grey)}

/* quote band */
.quote-band{left:0;top:624px;width:712px;height:125px;background:linear-gradient(90deg,#f2621a,#ff6a1e 55%,#f25a12)}
.quote-title{left:81px;top:655px;font-size:11px;font-weight:600;color:var(--white);letter-spacing:.3px}
.quote-text{left:81px;top:676px;width:380px;font-size:6.8px;line-height:14.5px;color:var(--white)}
.quote-text strong{font-weight:700}
.contact-btn{left:498px;top:670px;width:132px;height:37px;background:var(--navy);color:var(--white);font-size:9px;font-weight:700;display:flex;align-items:center;justify-content:center}

/* testimonials */
.testimonials-title{left:0;top:772px;width:712px;text-align:center;font-size:11px;font-weight:700;color:#4a4a4a}
.testimonial{width:170px;height:118px;top:820px;border:1px solid var(--line);background:var(--white)}
.testimonial .mark{position:absolute;left:16px;top:-11px;width:25px;height:21px;background:var(--white);border:1px solid var(--line);color:var(--orange);font-size:15px;font-weight:800;text-align:center;line-height:24px}
.testimonial p{position:absolute;left:16px;top:27px;width:145px;font-size:6.2px;line-height:11.3px;color:var(--grey)}
.testimonial .avatar{position:absolute;left:16px;top:72px;width:26px;height:26px;border-radius:50%;background:#000}
.testimonial .by{position:absolute;left:50px;top:76px;font-size:6px;color:var(--grey)}
.testimonial .name{position:absolute;left:50px;top:85px;font-size:6.4px;font-weight:700;color:#444;letter-spacing:.3px}
.t1{left:78px}.t2{left:268px}.t3{left:464px}

/* footer */
.site-footer{left:0;top:966px;width:712px;height:234px;background:var(--black)}
.skyline{left:0;top:1040px;width:712px;height:160px;background:linear-gradient(180deg,rgba(40,40,40,0),rgba(55,55,55,.55))}
.footer-head{font-size:6.6px;font-weight:700;color:var(--white);letter-spacing:.3px}
.quick-links{left:89px;top:1004px}
.quick-links ul{list-style:none;margin-top:9px}
.quick-links li{font-size:6.2px;color:var(--white);line-height:15px;font-weight:500}
.contact-col{left:218px;top:1004px}
.contact-row{position:absolute;left:0;display:flex;gap:8px;font-size:6.4px;line-height:12.5px;color:var(--white);white-space:nowrap}
.socials{position:absolute;left:2px;top:116px;display:flex;gap:7px}
.socials span{width:12px;height:12px;border-radius:50%}
.message-form{left:402px;top:1001px}
.field{position:absolute;background:var(--white);font-size:5.6px;color:#9a9a9a;padding:5px 6px}
.send-btn{position:absolute;left:0;top:151px;width:70px;height:19px;font-size:6px;font-weight:500;letter-spacing:.4px}
.copyright{left:81px;top:1164px;font-size:6.4px;color:var(--white)}
</style>
</head>
<body>

<header class="abs site-header">
  <div class="abs brand"><span class="brand-mark"></span>KPR Tidy Yard</div>
  <nav class="abs main-nav">
    <span>HOME</span><span>ABOUT US</span><span>SERVICES</span><span>OUR PROJECTS</span><span>REQUEST FREE QUOTE</span><span>CONTACT</span>
  </nav>
</header>

<section class="abs hero" role="img" aria-label="Worker polishing a tiled floor with an orange floor machine, seen from above"></section>
<div class="abs hero-photo"></div>
<svg class="abs hero-curve" width="712" height="52" viewBox="0 0 712 52" aria-hidden="true">
  <path d="M0 30 Q356 -14 712 22 L712 52 L0 52 Z" fill="#f0f5ee"/>
</svg>
<h1 class="abs hero-title">COMPREHENSIVE PORT-<br>CONSTRUCTION CLEANING</h1>
<p class="abs hero-text">Must explain to you how all this mistaken idea of denouncing pleasure and&nbsp; praising pain was born and I will give you a completed.</p>
<div class="abs btn-orange hero-btn">MORE DETAILS</div>
<svg class="abs slide-arrow slide-prev" viewBox="0 0 23 21" aria-label="Previous slide"><path d="M13 7 L9.5 10.5 L13 14" stroke="#fff" stroke-width="1.6" fill="none"/></svg>
<svg class="abs slide-arrow slide-next" viewBox="0 0 23 21" aria-label="Next slide"><path d="M10 7 L13.5 10.5 L10 14" stroke="#fff" stroke-width="1.6" fill="none"/></svg>

<section class="abs services-band"></section>
<article class="abs service-card card-labour">
  <div class="photo photo-site" role="img" aria-label="Construction workers cutting timber on a building site"></div>
  <div class="body"><h3>LABOUR</h3><p>Lorem ipsum dolor sit amet, consectetur ad-ipiscing elit, sed do eiusmod tempor Lorem ipsum dolor sit amet,</p></div>
</article>
<article class="abs service-card card-maintenance">
  <div class="photo photo-helmet" role="img" aria-label="Worker holding a yellow hard hat with a tool belt"></div>
  <div class="body"><h3>MAINTENANCE</h3><p>Lorem ipsum dolor sit amet, consectetur ad-ipiscing elit, sed do eiusmod tempor Lorem ipsum dolor sit amet,</p></div>
</article>
<article class="abs service-card card-cleaning">
  <div class="photo photo-wash" role="img" aria-label="Worker pressure washing a concrete floor"></div>
  <div class="body"><h3>CLEANING</h3><p>Lorem ipsum dolor sit amet, consectetur ad-ipiscing elit, sed do eiusmod tempor Lorem ipsum dolor sit amet,</p></div>
</article>

<h2 class="abs welcome-title">WELCOME TO KPR TIDY YARD</h2>
<p class="abs welcome-text">Lorem ipsum dolor sit amet, consectetur adipiscing elit, sed do eiusmod tempor incididunt ut labore et dolore magna aliqua. Ut enim ad minim veniam, quis nostrud exercitation ullamco laboris nisi ut aliquip ex ea commodo consequat. Duis aute irure dolor in reprehenderit in voluptate velit esse cillum dolore eu fugiat nulla pariatur. Excepteur sint occaecat cupidatat non proident, sunt in culpa qui officia deserunt mollit anim id est laborum</p>

<section class="abs quote-band" role="img" aria-label="Construction workers on site under an orange tint"></section>
<h2 class="abs quote-title">ARE YOU READY FOR A FREE QUOTE?</h2>
<p class="abs quote-text">We look forward to the opportunity of becoming a trusted and valued partner in improving and maintaining the appearance of your building. <strong>Call us 1-800-555-0142</strong> for all your commercial cleaning needs, and&nbsp; arrange your free estimate today.</p>
<div class="abs contact-btn">CONTACT US TODAY!</div>

<h2 class="abs testimonials-title">CLIENT TESTIMONIALS</h2>
<article class="abs testimonial t1"><span class="mark">&ldquo;</span><p>Industry's standard dummy text ever since the when an unknown printer took a galley of type and scrambled it to make.</p><span class="avatar"></span><span class="by">BY</span><span class="name">MARA OKONKWO</span></article>
<article class="abs testimonial t2"><span class="mark">&ldquo;</span><p>Industry's standard dummy text ever since the when an unknown printer took a galley of type and scrambled it to make.</p><span class="avatar"></span><span class="by">BY</span><span class="name">MARA OKONKWO</span></article>
<article class="abs testimonial t3"><span class="mark">&ldquo;</span><p>Industry's standard dummy text ever since the when an unknown printer took a galley of type and scrambled it to make.</p><span class="avatar"></span><span class="by">BY</span><span class="name">MARA OKONKWO</span></article>

<footer class="abs site-footer"></footer>
<div class="abs skyline" role="img" aria-label="Faint city skyline silhouette"></div>

<div class="abs quick-links">
  <div class="footer-head">QUICK LINKS</div>
  <ul><li>HOME</li><li>WHAT WE DO</li><li>OUR PRODUCTS</li><li>AREAS WE SERVE</li><li>ABOUT</li><li>CONTACT US</li></ul>
</div>

<div class="abs contact-col">
  <div class="footer-head">CONTACT US</div>
  <div class="contact-row" style="top:20px">
    <svg width="8" height="10" viewBox="0 0 8 10" style="margin-top:2px"><path d="M4 0 A4 4 0 0 1 8 4 C8 6.5 4 10 4 10 C4 10 0 6.5 0 4 A4 4 0 0 1 4 0 Z" fill="#ccc"/><circle cx="4" cy="4" r="1.4" fill="#050505"/></svg>
    <span>418 Larkin Avenue<br>Dover, OH 44622</span>
  </div>
  <div class="contact-row" style="top:60px">
    <svg width="8" height="8" viewBox="0 0 10 10" style="margin-top:2px"><path d="M2 0 L4 2.5 L3 4 Q4.5 6 6 7 L7.5 6 L10 8 L8.5 10 Q3 9 0 1.5 Z" fill="#ccc"/></svg>
    <span>+1 555 204 318</span>
  </div>
  <div class="contact-row" style="top:89px">
    <svg width="9" height="7" viewBox="0 0 9 7" style="margin-top:3px"><rect width="9" height="7" fill="#ccc"/><path d="M0 0 L4.5 4 L9 0" stroke="#050505" fill="none" stroke-width=".9"/></svg>
    <span>contact@kprtidyyard.com</span>
  </div>
  <div class="socials">
    <span style="background:#3b5998"></span><span style="background:#1da1f2"></span><span style="background:#dd4b39"></span><span style="background:#0077b5"></span>
  </div>
</div>

<form class="abs message-form">
  <div class="footer-head">LEAVE A MESSAGE</div>
  <div class="field" style="left:0;top:21px;width:112px;height:18px">First Name</div>
  <div class="field" style="left:120px;top:21px;width:112px;height:18px">Last Name</div>
  <div class="field" style="left:0;top:47px;width:112px;height:18px">Email</div>
  <div class="field" style="left:120px;top:47px;width:112px;height:18px">Date</div>
  <div class="field" style="left:0;top:74px;width:232px;height:69px">Your Message</div>
  <div class="btn-orange send-btn">SEND MESSAGE</div>
</form>

<p class="abs copyright">&copy;2019 kprtidyyard.com. All Rights Reserved</p>

</body>
</html>
```